Hotdogs & Burgers restaurant needs a new menu design

We need a new menu design for our restaurant "Pupvella". Pupvella is a fast food specialized in hotdogs and burgers.We are looking for a simple easy menu design that walk through our customer to order the sandwich ==> the fries =>> the sides and the drinks. Pupvella Menu:* Sandwiches**Hotdogs Our special fresh grilled hotdog served on fresh buns (Regular – 1.300 OMR / Franks – 2.000 OMR)*** DoganzaLettuce, tomato, jalapeno, pickle, onion, corn, chips, cheese, ketchup, mayo, mustard*** PepperBell pepper, onion, sweet chili sauce, avocado*** Chili FlamesChili carne, cheddar cheese, honey mustard*** ChicagoTomato, pickle, red onion, sweet relish, mustard*** New YorkGrilled onion, beef bacon, barbecue sauce, chili mustard*** Egg & CheeseOmelet, cheese, ketchup, mayo, mustard** Burgers 100% all natural beef & freshly ground, 100 grams each patty served on fresh buns.(Single patty - 2.000 OMR / double patty - 2.500 OMR)*** Sweet Beef BurgerBeef bacon, cheese, lettuce, tomato, pickle.*** Cheese Beef BurgerCheese, pickle, Pupvella sauce.*** Mexican Beef BurgerGuacamole sauce, red onion, lettuce, tomato, Pupvella sauce.*** Chicken BurgerFried chicken patty, lettuce, tomato, ranch sauce, Pupvella sauce== ToppingsExtra veggies 0.100 OMRExtra cheese 0.200 OMRExtra beef Bacon 0.400 OMRExtra patty 0.500 OMR*Fries**Regular 0.600 OMR**Crispy 0.800 OMR**Wedges 0.800 OMR**Chili fries 1.500 OMRTopped with our chili carne, cheddar cheese, jalapeno, honey mustard**Lava fries 1.500 OMRTopped with fried bacon, fried onion, cheddar cheese, ranch sauce*Sides**Crispy strips 1.800 OMR5 pieces of chicken strips topped with BBQ sauce or honey mustard sauce, Pupvella side sauce**Jalapeno cheese balls 1.300 OMR6 pieces of jalapeno cheese balls, sweet chili side sauce**Nachos 1.500 OMRA plate of nachos topped with cheddar cheese and jalapeno*Drinks**Flavored sparkling cans 0.800 OMR **Fresh orange juice 1.400 OMR**Mineral water 0.300 OMR**Soft drink 0.400 OMR**Mojito 1.500 OMRThe menu should not have any of our products pictures (icons/symbols proffered). we would prefer if the designs have unique icons/symbols created for Pupvella. you can check our Picturo page https://www.picturo-app.example/pupvella.official/

Industry/Entity Type

American Restaurant

Colors

Designer to choose colors to be used in the design.

Requirements
Must have
• Pupvella Logo, Icons

```html
<!DOCTYPE html>
<html lang="en">
<head>
<meta charset="utf-8">
<title>Pupvella Menu</title>
<link href="https://fonts.googleapis.com/css2?family=Alfa+Slab+One&family=Lilita+One&family=Noto+Serif&family=Montserrat:wght@400;700&family=Roboto+Condensed:wght@400&display=swap" rel="stylesheet">
<style>
:root{
  --paper:#ffffff;
  --board:#0d0b0d;
  --board-glow:#2b262b;
  --ink:#f2f2f2;
  --accent:#f5e600;
  --price:#e9dc1a;
  --leader:#d8d8d8;
}
*{margin:0;padding:0;box-sizing:border-box}
html,body{width:865px;height:1200px;overflow:hidden;background:var(--paper)}
.menu{position:absolute;left:15px;top:15px;width:834px;height:1170px;
  background:radial-gradient(ellipse at 50% 42%,var(--board-glow) 0%,#141114 55%,var(--board) 100%);
  color:var(--ink);font-family:"Montserrat",sans-serif}
.abs{position:absolute}
.menu-title{left:0;width:834px;top:12px;text-align:center;font-family:"Alfa Slab One",serif;font-size:40px;line-height:44px;color:var(--ink);letter-spacing:1px}
.title-rule{top:32px;height:2px;background:var(--ink)}
.brand{left:0;width:834px;top:115px;text-align:center;font-family:"Lilita One",sans-serif;font-size:42px;line-height:46px;color:var(--accent)}
.section-title{font-family:"Lilita One",sans-serif;color:var(--accent);font-size:28px;line-height:30px;padding-bottom:2px;border-bottom:1.5px solid var(--accent)}
.section-title.plain{border-bottom:none;padding-bottom:0}
.intro{font-size:12px;line-height:13.5px;color:var(--ink);padding-bottom:5px;border-bottom:1.5px solid var(--accent)}
.col-label{font-family:"Roboto Condensed",sans-serif;font-size:10.5px;width:80px;text-align:center;margin-left:-40px}
.row{display:flex;align-items:flex-end;height:18px}
.item-name{font-family:"Noto Serif",serif;font-size:16px;line-height:18px;white-space:nowrap}
.leader{flex:1;border-bottom:1px dashed var(--leader);margin-bottom:4px}
.price{position:absolute;top:1px;font-family:"Roboto Condensed",sans-serif;font-size:9.5px;color:var(--price);width:40px;text-align:center;margin-left:-20px}
.desc{font-size:11px;line-height:13.5px;color:#e8e8e8}
.subhead{font-family:"Lilita One",sans-serif;font-size:22px;color:var(--ink);letter-spacing:.5px;border-bottom:1.5px solid var(--accent);line-height:24px}
.topping{width:110px;margin-left:-55px;text-align:center}
.topping-art{width:44px;height:36px;margin:0 auto 8px;border-radius:8px}
.topping-name{font-weight:700;font-size:12px;color:var(--accent);line-height:14px}
.topping-price{font-weight:700;font-size:9.5px;line-height:14px}
</style>
</head>
<body>
<main class="menu">
  <header>
    <div class="abs title-rule" style="left:302px;width:44px"></div>
    <svg class="abs" style="left:280px;top:25px" width="22" height="16" viewBox="0 0 22 16" aria-hidden="true"><rect x="1" y="3" width="14" height="10" rx="1.5" fill="none" stroke="#f2f2f2" stroke-width="1.6"/><line x1="4" y1="6" x2="12" y2="6" stroke="#f2f2f2" stroke-width="1"/><line x1="4" y1="10" x2="12" y2="10" stroke="#f2f2f2" stroke-width="1"/><line x1="15" y1="8" x2="22" y2="8" stroke="#f2f2f2" stroke-width="2"/></svg>
    <h1 class="abs menu-title">MENU</h1>
    <div class="abs title-rule" style="left:503px;width:36px"></div>
    <svg class="abs" style="left:538px;top:26px" width="22" height="14" viewBox="0 0 22 14" aria-hidden="true"><path d="M21 3H8M21 11H8M8 3Q3 3 3 7Q3 11 8 11" fill="none" stroke="#f2f2f2" stroke-width="1.6"/><line x1="0" y1="7" x2="3" y2="7" stroke="#f2f2f2" stroke-width="2"/></svg>
    <div class="abs brand">Pupvella</div>
  </header>

  <section>
    <h2 class="abs section-title plain" style="left:30px;top:176px">Burgers</h2>
    <p class="abs intro" style="left:30px;top:212px;width:270px">100% all natural beef &amp; freshly ground,<br>100 grams each patty served on fresh buns.</p>
    <div class="abs col-label" style="left:249px;top:256px">Single patty</div>
    <div class="abs col-label" style="left:338px;top:256px">Double patty</div>

    <div class="abs row" style="left:30px;top:279px;width:380px"><span class="item-name">Sweet Beef Burger</span><span class="leader"></span><span class="price" style="left:220px">2.00</span><span class="price" style="left:308px">2.50</span></div>
    <p class="abs desc" style="left:30px;top:299px">Beef bacon, cheese,<br>lettuce, tomato, pickle.</p>

    <div class="abs row" style="left:30px;top:337px;width:380px"><span class="item-name">Cheese Beef Burger</span><span class="leader"></span><span class="price" style="left:220px">2.00</span><span class="price" style="left:308px">2.50</span></div>
    <p class="abs desc" style="left:30px;top:356px">Cheese, pickle, Pupvella sauce.</p>

    <div class="abs row" style="left:30px;top:379px;width:380px"><span class="item-name">Mexican Beef Burger</span><span class="leader"></span><span class="price" style="left:220px">2.00</span><span class="price" style="left:308px">2.50</span></div>
    <p class="abs desc" style="left:30px;top:398px">Fried chicken patty, lettuce, tomato,<br>ranch sauce, Pupvella sauce.</p>

    <div class="abs row" style="left:30px;top:436px;width:380px"><span class="item-name">Chicken Burger</span><span class="leader"></span><span class="price" style="left:220px">2.00</span><span class="price" style="left:308px">2.50</span></div>
    <p class="abs desc" style="left:30px;top:456px">Tomato, pickle, red onion, sweet relish, mustard</p>
  </section>

  <section>
    <h2 class="abs subhead" style="left:152px;top:503px">SANDWICHES</h2>
    <h2 class="abs section-title plain" style="left:30px;top:538px">Hot Dogs</h2>
    <p class="abs intro" style="left:30px;top:574px;width:242px">Our special fresh grilled hotdog served<br>on fresh buns</p>
    <div class="abs col-label" style="left:249px;top:615px">Regular</div>
    <div class="abs col-label" style="left:338px;top:617px">Franks</div>

    <div class="abs row" style="left:30px;top:645px;width:380px"><span class="item-name">Pupvella</span><span class="leader"></span><span class="price" style="left:220px">1.30</span><span class="price" style="left:308px">2.00</span></div>
    <p class="abs desc" style="left:30px;top:665px">Lettuce, tomato, jalapeno, pickle, onion, corn, chips,<br>cheese, ketchup, mayo, mustard</p>

    <div class="abs row" style="left:30px;top:710px;width:380px"><span class="item-name">Pepper</span><span class="leader"></span><span class="price" style="left:220px">1.30</span><span class="price" style="left:308px">2.00</span></div>
    <p class="abs desc" style="left:30px;top:731px">Bell pepper, onion, sweet chili sauce, avocado</p>

    <div class="abs row" style="left:30px;top:771px;width:380px"><span class="item-name">Chili Flames</span><span class="leader"></span><span class="price" style="left:220px">1.30</span><span class="price" style="left:308px">2.00</span></div>
    <p class="abs desc" style="left:30px;top:791px">Chili carne, cheddar cheese, honey mustard</p>

    <div class="abs row" style="left:30px;top:832px;width:380px"><span class="item-name">Chicago</span><span class="leader"></span><span class="price" style="left:220px">1.30</span><span class="price" style="left:308px">2.00</span></div>
    <p class="abs desc" style="left:30px;top:851px">Tomato, pickle, red onion, sweet relish, mustard</p>

    <div class="abs row" style="left:30px;top:885px;width:380px"><span class="item-name">New York</span><span class="leader"></span><span class="price" style="left:220px">1.30</span><span class="price" style="left:308px">2.00</span></div>
    <p class="abs desc" style="left:30px;top:904px">Grilled onion, beef bacon,<br>barbecue sauce, chili mustard</p>

    <div class="abs row" style="left:30px;top:951px;width:380px"><span class="item-name">Egg &amp; Cheese</span><span class="leader"></span><span class="price" style="left:220px">1.30</span><span class="price" style="left:308px">2.00</span></div>
    <p class="abs desc" style="left:30px;top:972px">Omelet, cheese, ketchup, mayo, mustard</p>
  </section>

  <section>
    <h2 class="abs section-title" style="left:450px;top:178px">Sides</h2>
    <div class="abs row" style="left:450px;top:239px;width:336px"><span class="item-name">Crispy strips</span><span class="leader"></span><span class="price" style="left:239px">1.80</span></div>
    <p class="abs desc" style="left:450px;top:260px">5 pieces of chicken strips topped<br>with BBQ sauce or honey mustard sauce,<br>Pupvella side sauce</p>
    <div class="abs row" style="left:450px;top:316px;width:336px"><span class="item-name">Jalapeno cheese balls</span><span class="leader"></span><span class="price" style="left:239px">1.30</span></div>
    <p class="abs desc" style="left:450px;top:336px">6 pieces of jalapeno cheese balls,<br>sweet chili side sauce</p>
    <div class="abs row" style="left:450px;top:386px;width:336px"><span class="item-name">Nachos</span><span class="leader"></span><span class="price" style="left:239px">1.50</span></div>
    <p class="abs desc" style="left:450px;top:407px">A plate of nachos topped with<br>cheddar cheese and jalapeno</p>
  </section>

  <section>
    <h2 class="abs section-title" style="left:450px;top:459px">Fries</h2>
    <div class="abs row" style="left:450px;top:507px;width:336px"><span class="item-name">Regular</span><span class="leader"></span><span class="price" style="left:239px">0.60</span></div>
    <div class="abs row" style="left:450px;top:541px;width:336px"><span class="item-name">Crispy</span><span class="leader"></span><span class="price" style="left:239px">0.80</span></div>
    <div class="abs row" style="left:450px;top:580px;width:336px"><span class="item-name">Wedges</span><span class="leader"></span><span class="price" style="left:239px">0.80</span></div>
    <div class="abs row" style="left:450px;top:611px;width:336px"><span class="item-name">Chili fries</span><span class="leader"></span><span class="price" style="left:239px">1.50</span></div>
    <p class="abs desc" style="left:450px;top:630px">Topped with our chili carne,<br>cheddar cheese, jalapeno, honey mustard</p>
    <div class="abs row" style="left:450px;top:668px;width:336px"><span class="item-name">Lava fries</span><span class="leader"></span><span class="price" style="left:239px">1.50</span></div>
    <p class="abs desc" style="left:450px;top:689px">Topped with fried bacon, fried onion,<br>cheddar cheese, ranch sauce</p>
  </section>

  <section>
    <h2 class="abs section-title" style="left:450px;top:740px">Drinks</h2>
    <div class="abs row" style="left:450px;top:795px;width:336px"><span class="item-name">Flavored sparkling cans</span><span class="leader"></span><span class="price" style="left:239px">0.80</span></div>
    <div class="abs row" style="left:450px;top:838px;width:336px"><span class="item-name">Fresh orange juice</span><span class="leader"></span><span class="price" style="left:239px">1.40</span></div>
    <div class="abs row" style="left:450px;top:881px;width:336px"><span class="item-name">Mineral water</span><span class="leader"></span><span class="price" style="left:239px">0.30</span></div>
    <div class="abs row" style="left:450px;top:924px;width:336px"><span class="item-name">Soft drink</span><span class="leader"></span><span class="price" style="left:239px">0.40</span></div>
    <div class="abs row" style="left:450px;top:967px;width:336px"><span class="item-name">Mojito</span><span class="leader"></span><span class="price" style="left:239px">1.50</span></div>
  </section>

  <section>
    <h2 class="abs section-title" style="left:324px;top:1008px">Extra Toppings</h2>
    <div class="abs topping" style="left:271px;top:1062px">
      <div class="topping-art" role="img" aria-label="Veggies illustration" style="background:radial-gradient(circle,#e0523a 0%,#6aa84f 70%)"></div>
      <div class="topping-name">VEGGIES</div><div class="topping-price">0.100 OMR</div>
    </div>
    <div class="abs topping" style="left:365px;top:1062px">
      <div class="topping-art" role="img" aria-label="Cheese wedge illustration" style="background:linear-gradient(#ffe05a,#f2b632)"></div>
      <div class="topping-name">CHEESE</div><div class="topping-price">0.200 OMR</div>
    </div>
    <div class="abs topping" style="left:459px;top:1062px">
      <div class="topping-art" role="img" aria-label="Beef patties illustration" style="background:linear-gradient(#6b5a52,#3f3430)"></div>
      <div class="topping-name">PATTY</div><div class="topping-price">0.500 OMR</div>
    </div>
    <div class="abs topping" style="left:552px;top:1062px">
      <div class="topping-art" role="img" aria-label="Beef bacon strips illustration" style="background:linear-gradient(#f6c2c2,#d9534f)"></div>
      <div class="topping-name">BEEF BACON</div><div class="topping-price">0.400 OMR</div>
    </div>
  </section>
</main>
</body>
</html>
```